Halloway Crest Backers Guild business cards

Create a single-sided business card for the Halloway Crest Backers Guild based on the attached logo.
The additional data fields include Name, Title, Email, Phone, and website.
Please use the following as sample data:
Name: Dean Varrow
Title: Co-Founder / Investor
Email: deanvarrow@mailtern.net
Phone: 555-314-2706
Website: www.hcbackersguild.com

Target Market(s)

Start ups, entrepreneurs, venture capitalists

Industry/Entity Type

Investment

Contact Information for Business Card

Professional business card. Technology company.

Font styles to use
Serif
Sans Serif

Requirements
Must have
• Include the HCBG logo (attached)
• Name
• Title
• Email
• Phone
• Website
Should not have
• Cute, cartoony

```html
<!DOCTYPE html>
<html lang="en">
<head>
<meta charset="utf-8">
<title>Halloway Crest Backers Guild – Business Card</title>
<link rel="stylesheet" href="https://fonts.googleapis.com/css2?family=Open+Sans:wght@400;600;700&display=swap">
<style>
  :root {
    --backdrop: #c8c8ca;
    --card-white: #ffffff;
    --card-black: #121212;
    --card-charcoal: #2a2a2a;
    --brand-green: #3aa455;
    --lime: #b5e36a;
    --deep-green: #1f7a32;
    --ink-light: #f2f2f2;
    --guild-grey: #6c6c6c;
  }
  * { margin: 0; padding: 0; box-sizing: border-box; }
  html, body { width: 1200px; height: 863px; overflow: hidden; }
  body {
    background: var(--backdrop);
    font-family: "Open Sans", Arial, sans-serif;
    position: relative;
  }
  .card {
    position: absolute;
    left: 320px;
    width: 560px;
    height: 320px;
    border-radius: 22px;
    overflow: hidden;
    box-shadow: 0 10px 24px rgba(0,0,0,0.25);
  }
  .card--back {
    top: 80px;
    background: linear-gradient(160deg, var(--card-charcoal) 0%, var(--card-black) 55%, #050505 100%);
  }
  .card--front {
    top: 460px;
    background: var(--card-white);
  }
  .card__art { position: absolute; inset: 0; }

  .brand {
    position: absolute;
    display: flex;
    align-items: center;
    gap: 14px;
  }
  .brand__mark {
    width: 34px; height: 34px;
    border-radius: 50%;
    background: var(--brand-green);
    flex: none;
  }
  .brand__name {
    color: var(--brand-green);
    font-weight: 600;
    font-size: 25px;
    line-height: 1.1;
    letter-spacing: 0.3px;
    border-left: 1px solid var(--brand-green);
    padding-left: 14px;
  }
  .card--back .brand { left: 150px; top: 118px; }
  .card--front .brand { left: 210px; top: 62px; }
  .card--front .brand__name { font-size: 23px; }

  .contact {
    position: absolute;
    left: 0; top: 150px;
    transform-origin: 0 0;
    transform: rotate(12.3deg);
    padding: 12px 0 0 40px;
    color: var(--ink-light);
  }
  .contact__headline { font-size: 15px; white-space: nowrap; }
  .contact__name { font-weight: 700; }
  .contact__title { color: var(--brand-green); font-weight: 400; }
  .contact__line {
    font-size: 11.5px;
    line-height: 19px;
    display: flex;
    align-items: center;
    gap: 6px;
    white-space: nowrap;
  }
  .contact__icon { width: 12px; height: 12px; flex: none; }
  .contact__line--plain { padding-left: 18px; }
</style>
</head>
<body>

<section class="card card--back">
  <div class="brand">
    <span class="brand__mark"></span>
    <span class="brand__name">Halloway Crest<br>Backers Guild</span>
  </div>
</section>

<section class="card card--front">
  <svg class="card__art" viewBox="0 0 560 320" width="560" height="320" aria-hidden="true">
    <defs>
      <linearGradient id="stripe" x1="0" y1="0" x2="1" y2="0">
        <stop offset="0" stop-color="#1f7a32"/>
        <stop offset="0.5" stop-color="#b5e36a"/>
        <stop offset="1" stop-color="#3aa455"/>
      </linearGradient>
      <linearGradient id="band" x1="0" y1="0" x2="1" y2="0">
        <stop offset="0" stop-color="#0c0c0c"/>
        <stop offset="0.6" stop-color="#1a1a1a"/>
        <stop offset="1" stop-color="#3a3a3a"/>
      </linearGradient>
    </defs>
    <polygon points="0,150 560,272 560,320 0,320" fill="url(#band)"/>
    <line x1="0" y1="148" x2="560" y2="270" stroke="url(#stripe)" stroke-width="4"/>
  </svg>

  <div class="brand">
    <span class="brand__mark"></span>
    <span class="brand__name">Halloway Crest<br>Backers Guild</span>
  </div>

  <div class="contact">
    <p class="contact__headline"><span class="contact__name">Dean Varrow</span> <span class="contact__title">| Co-Founder / Investor</span></p>
    <p class="contact__line contact__line--plain">www.hcbackersguild.com</p>
    <p class="contact__line">
      <svg class="contact__icon" viewBox="0 0 12 12"><rect x="3" y="0.5" width="6" height="11" rx="1.2" fill="none" stroke="#f2f2f2" stroke-width="1.2"/><line x1="5" y1="9.5" x2="7" y2="9.5" stroke="#f2f2f2" stroke-width="1"/></svg>
      555-314-2706
    </p>
    <p class="contact__line">
      <svg class="contact__icon" viewBox="0 0 12 12"><rect x="0.6" y="2.5" width="10.8" height="7.5" fill="none" stroke="#f2f2f2" stroke-width="1.2"/><polyline points="0.8,2.8 6,7 11.2,2.8" fill="none" stroke="#f2f2f2" stroke-width="1.2"/></svg>
      deanvarrow@mailtern.net
    </p>
  </div>
</section>

</body>
</html>
```